Business Cards and Stationery incorporating Logo design
Business Cards and Stationery incorporating Logo design -
Creative Brief
Professional
Daniel P. Halvorsen
Managing Director
418 Corvane Tower 9th Fl. Marlow Heights, OH 44021
1-555-hdg-cash
dhalvorsen@halvorsendrakeco.example
www.halvorsendrakeco.example

```html
<!DOCTYPE html>
<html lang="en">
<head>
<meta charset="utf-8">
<title>Halvorsen Drake – Business Cards</title>
<link rel="stylesheet" href="https://fonts.googleapis.com/css2?family=Marcellus&family=Open+Sans:wght@400;600;700&display=swap">
<style>
  :root {
    --backdrop: #4a3a2e;
    --card-white: #ffffff;
    --brand-green: #1f6b3d;
    --ink: #111111;
    --text-gray: #555555;
  }
  * { margin: 0; padding: 0; box-sizing: border-box; }
  html, body { width: 1200px; height: 760px; overflow: hidden; }
  body { background: var(--backdrop); position: relative; font-family: "Open Sans", Arial, sans-serif; }

  .card {
    position: absolute;
    width: 496px;
    height: 288px;
    border-radius: 12px;
    overflow: hidden;
    box-shadow: 0 6px 14px rgba(0,0,0,0.35);
  }
  .card--front { left: 76px; top: 120px; background: var(--card-white); }
  .card--back { left: 584px; top: 120px; background: var(--card-white); }
  .card--green { left: 312px; top: 414px; background: var(--brand-green); }

  .brand {
    position: absolute;
    display: flex;
    align-items: center;
    gap: 14px;
  }
  .brand__square { width: 60px; height: 60px; background: var(--ink); flex: none; }
  .brand__rule { width: 2px; height: 70px; background: var(--ink); flex: none; }
  .brand__name {
    font-family: "Marcellus", Georgia, serif;
    font-size: 38px;
    line-height: 0.95;
    color: var(--ink);
    letter-spacing: 0.5px;
  }
  .card--front .brand { left: 157px; top: 34px; }
  .card--back .brand { left: 57px; top: 104px; }
  .card--back .brand__name { font-size: 48px; }
  .card--back .brand__square { width: 76px; height: 76px; }
  .card--back .brand__rule { height: 90px; }
  .card--green .brand { left: 60px; top: 104px; }
  .card--green .brand__name { font-size: 46px; color: var(--card-white); }
  .card--green .brand__square { width: 78px; height: 66px; }
  .card--green .brand__rule { height: 86px; background: var(--card-white); }

  .contact {
    position: absolute;
    left: 22px;
    font-size: 11.5px;
    line-height: 1.45;
    color: var(--text-gray);
  }
  .contact--address { top: 118px; }
  .contact--lines { top: 158px; }
  .contact--web { top: 236px; }

  .person { position: absolute; left: 238px; top: 148px; }
  .person__name { font-size: 19px; font-weight: 700; color: var(--brand-green); }
  .person__title { font-size: 13.5px; color: var(--text-gray); }

  .front-band { position: absolute; left: 0; bottom: 0; width: 496px; height: 24px; }
</style>
</head>
<body>

  <section class="card card--front" aria-label="Business card front">
    <div class="brand">
      <span class="brand__square"></span>
      <span class="brand__rule"></span>
      <span class="brand__name">Halvorsen<br>Drake</span>
    </div>

    <p class="contact contact--address">418 Corvane Tower 9th Fl.<br>Marlow Heights, OH 44021</p>
    <p class="contact contact--lines">
      T: 1-555-hdg-cash<br>
      P: (555) 240-1187<br>
      C: (555) 318-6042<br>
      E: dhalvorsen@halvorsendrakeco.example
    </p>
    <p class="contact contact--web">W: www.halvorsendrakeco.example</p>

    <div class="person">
      <p class="person__name">Daniel P. Halvorsen</p>
      <p class="person__title">Managing Director</p>
    </div>

    <svg class="front-band" viewBox="0 0 496 24" preserveAspectRatio="none" aria-hidden="true">
      <polygon points="0,12 330,12 342,0 496,0 496,24 0,24" fill="var(--brand-green)"/>
      <polygon points="350,0 420,0 400,24 330,24" fill="var(--ink)"/>
    </svg>
  </section>

  <section class="card card--back" aria-label="Business card back, white">
    <div class="brand">
      <span class="brand__square"></span>
      <span class="brand__rule"></span>
      <span class="brand__name">Halvorsen<br>Drake</span>
    </div>
  </section>

  <section class="card card--green" aria-label="Business card back, green">
    <div class="brand">
      <span class="brand__square"></span>
      <span class="brand__rule"></span>
      <span class="brand__name">Halvorsen<br>Drake</span>
    </div>
  </section>

</body>
</html>
```